Northern Tempest Informational Sheet

I need a one page informational sheet (advertisement) for a horse called Northern Tempest. It should have the name Northern Tempest and the content below. It needs to be eye-catching. I have attached 3 examples of what these advertisements look like so it's easier to create. I've also attached 2 pictures of the horse which should both be used in the advertisement.

Here are the bullet points:

- Son of Distant Harbor with total progeny earnings over 13 million dollars
- Ranks among West Virginia top 3 active sires by progeny earnings 2019
- In 9 crops of racing age, has sired 200 winners from 275 starters
- Sired Don Marbellino who earned over $800k racing from age 2 to 7.
- Won 3 of 4 lifetime starts

stands at stud for $1000 at Ashgrove Farm near Charles Town
Call Dwight Kessler - (304) 555-0193

Target Market(s)

Thoroughbred racing people interested in breeding

Requirements
Must have
• Unique and creative. The name of the horse Northern Tempest should be clear and bold, the picture should also be prominent.
Should not have
• Cartoon like, whimsical

```html
<!DOCTYPE html>
<html lang="en">
<head>
<meta charset="UTF-8">
<title>Northern Tempest – Stallion Sheet</title>
<link href="https://fonts.googleapis.com/css2?family=Oswald:wght@700&family=Montserrat:wght@500;600;700&display=swap" rel="stylesheet">
<style>
  :root {
    --ink: #0e0d0c;
    --ink-soft: #1c1a18;
    --gold: #fcd82f;
    --red: #c8101a;
    --red-text: #d3131c;
    --white: #ffffff;
    --bay-dark: #3b1f10;
    --bay: #8a4a22;
    --sky: #a9a49a;
  }
  * { box-sizing: border-box; margin: 0; padding: 0; }
  html, body { width: 882px; height: 1200px; overflow: hidden; background: var(--ink); }
  .sheet {
    position: relative; width: 882px; height: 1200px; overflow: hidden;
    background: radial-gradient(ellipse at 50% 70%, var(--ink-soft), var(--ink) 70%);
    font-family: "Montserrat", Arial, sans-serif; color: var(--white);
  }
  .hero-photo {
    position: absolute; left: 0; top: 0; width: 882px; height: 560px;
    background:
      linear-gradient(to bottom, rgba(14,13,12,0) 55%, var(--ink) 100%),
      radial-gradient(ellipse 38% 30% at 50% 42%, var(--bay) 0%, var(--bay-dark) 60%, transparent 75%),
      linear-gradient(to right, var(--sky) 0%, #7c776c 55%, #8f4a36 72%, #7a3b2b 100%);
  }
  .horse-name {
    position: absolute; left: 0; top: 515px; width: 882px;
    font-family: "Oswald", "Arial Narrow", sans-serif; font-weight: 700;
    font-size: 104px; line-height: 1; color: var(--gold);
    text-align: center; white-space: nowrap; letter-spacing: -1px;
    transform: scaleY(1.12); transform-origin: top center;
  }
  .sire-box {
    position: absolute; left: 50px; top: 662px; width: 396px; height: 101px;
    background: var(--red); text-align: center;
    font-weight: 700; font-size: 18.5px; line-height: 29px; padding-top: 7px;
    text-transform: uppercase;
  }
  .sire-box .hl { color: var(--gold); }
  .facts { position: absolute; left: 30px; top: 795px; width: 440px; list-style: none; }
  .fact {
    position: relative; text-align: center; font-size: 19px; font-weight: 500;
    line-height: 29px; margin-bottom: 16px;
  }
  .fact .star { position: absolute; left: 0; top: 4px; width: 24px; height: 24px; fill: var(--gold); }
  .fact.first .star { top: 36px; }
  .fact .y { color: var(--gold); font-weight: 700; }
  .fact .r { color: var(--red-text); font-weight: 700; }
  .fact .big { font-size: 24px; }
  .fact.last { font-size: 24px; margin-top: 6px; }
  .fact.last .star { top: 2px; }
  .portrait-frame {
    position: absolute; left: 512px; top: 660px; width: 308px; height: 410px;
    border: 7px solid var(--gold);
  }
  .portrait-photo {
    width: 100%; height: 100%;
    background:
      radial-gradient(ellipse 45% 55% at 50% 62%, var(--bay) 0%, var(--bay-dark) 65%, transparent 80%),
      linear-gradient(to bottom, #b0593b 0%, #6d6e6c 18%, #4c4d4c 100%);
  }
  .stud-fee {
    position: absolute; left: 30px; top: 1112px; width: 440px; text-align: center;
    font-size: 20px; font-weight: 500; line-height: 31px;
  }
  .stud-fee .y { color: var(--gold); font-weight: 700; }
  .stud-fee .r { color: var(--red-text); }
  .contact { position: absolute; left: 468px; top: 1100px; width: 414px; height: 100px; }
  .contact svg.band { position: absolute; inset: 0; }
  .contact-text {
    position: absolute; left: 30px; right: 0; top: 22px; text-align: center;
    font-weight: 700; font-size: 22px; line-height: 32px;
  }
  .contact-text .who { color: var(--gold); text-transform: uppercase; }
  .contact-text .phone { font-weight: 600; }
  .contact-text .phone svg { width: 18px; height: 18px; vertical-align: -2px; margin-right: 6px; }
</style>
</head>
<body>
<main class="sheet">
  <div class="hero-photo" role="img" aria-label="Photo of Northern Tempest, a bay stallion in a halter, standing in profile outside a brick barn"></div>

  <h1 class="horse-name">NORTHERN TEMPEST</h1>

  <div class="sire-box">
    Son of Distant Harbor with<br>
    <span class="hl">total progeny earnings<br>over 13 million dollars</span>
  </div>

  <ul class="facts">
    <li class="fact first">
      <svg class="star" viewBox="0 0 24 24"><path d="M12 1l3.2 7.2 7.8.7-5.9 5.2 1.8 7.7L12 17.8 5.1 21.8l1.8-7.7L1 8.9l7.8-.7z"/></svg>
      Ranks among West Virginia<br>
      <span class="y">Top 3 active sires</span> <b>by progeny</b><br>
      <span class="r big">Earnings 2019</span>
    </li>
    <li class="fact">
      <svg class="star" viewBox="0 0 24 24"><path d="M12 1l3.2 7.2 7.8.7-5.9 5.2 1.8 7.7L12 17.8 5.1 21.8l1.8-7.7L1 8.9l7.8-.7z"/></svg>
      In 9 crops of racing age, has sired<br>
      <span class="y">200 winners from 275 starters</span>
    </li>
    <li class="fact">
      <svg class="star" viewBox="0 0 24 24"><path d="M12 1l3.2 7.2 7.8.7-5.9 5.2 1.8 7.7L12 17.8 5.1 21.8l1.8-7.7L1 8.9l7.8-.7z"/></svg>
      <span class="r">Sired Don Marbellino who earned</span><br>
      <b>over <span class="y">$800k</span> racing from age 2 to 7.</b>
    </li>
    <li class="fact last">
      <svg class="star" viewBox="0 0 24 24"><path d="M12 1l3.2 7.2 7.8.7-5.9 5.2 1.8 7.7L12 17.8 5.1 21.8l1.8-7.7L1 8.9l7.8-.7z"/></svg>
      <span class="r">Won 3</span> <span class="y">of 4</span> lifetime starts
    </li>
  </ul>

  <div class="portrait-frame">
    <div class="portrait-photo" role="img" aria-label="Photo of Northern Tempest in a halter, head and shoulders, in front of a barn door"></div>
  </div>

  <p class="stud-fee">
    stands at stud for <span class="y">$1000</span> at<br>
    <span class="r">Ashgrove Farm near Charles Town</span>
  </p>

  <div class="contact">
    <svg class="band" viewBox="0 0 414 100" preserveAspectRatio="none">
      <polygon points="0,0 414,0 414,100 30,100" fill="var(--white)"/>
      <polygon points="8,6 414,6 414,100 38,100" fill="var(--red)"/>
    </svg>
    <div class="contact-text">
      <div class="who">Call Dwight Kessler</div>
      <div class="phone">
        <svg viewBox="0 0 24 24" fill="none" stroke="#fff" stroke-width="2"><path d="M5 3h4l2 5-2.5 1.5a11 11 0 005 5L15 12l5 2v4a2 2 0 01-2 2A16 16 0 013 5a2 2 0 012-2z"/></svg>(304) 555-0193
      </div>
    </div>
  </div>
</main>
</body>
</html>
```